business card for a massage therapy practice named 'Meadow and Willow Massage Studio'

I really need a trendy, yet easy on the eyes business card to complement my logo. Ideally with some gold or rose gold foil work.

My uploaded file of the logo I have in horizontal but I have a vertical version as well. Another color that is used in the website is a blush pink here and there. I'd like to see some trendy tropical leaves in the design.

```html
<!DOCTYPE html>
<html lang="en">
<head>
<meta charset="utf-8">
<title>Meadow and Willow Massage Studio — Business Card</title>
<link rel="stylesheet" href="https://fonts.googleapis.com/css2?family=Montserrat:wght@400;500;600&display=swap">
<style>
  :root {
    --backdrop: #e4e4e4;
    --card-black: #1a1613;
    --card-edge: #231d19;
    --gold: #c99a3e;
    --gold-light: #f1d27a;
    --gold-deep: #8a6420;
    --blush: #e8b4ad;
    --blush-soft: rgba(232, 180, 173, 0.18);
    --text-soft: #d8d2c8;
    --leaf-tone: #43352a;
  }
  * { box-sizing: border-box; margin: 0; padding: 0; }
  html, body {
    width: 1200px;
    height: 800px;
    overflow: hidden;
    background: var(--backdrop);
    font-family: "Montserrat", sans-serif;
  }
  .sheet {
    width: 1200px;
    height: 800px;
    display: flex;
    align-items: center;
    justify-content: center;
    gap: 60px;
  }
  .card {
    position: relative;
    width: 525px;
    height: 300px;
    background: radial-gradient(ellipse at 40% 40%, var(--card-edge), var(--card-black) 75%);
    box-shadow: 0 18px 40px rgba(0, 0, 0, 0.25);
    overflow: hidden;
  }

  /* Front */
  .leaf-decoration {
    position: absolute;
    right: 20px;
    top: -30px;
    width: 320px;
    height: 260px;
    border-radius: 48% 52% 40% 60%;
    background:
      radial-gradient(ellipse at 35% 45%, var(--blush-soft) 0%, rgba(232, 180, 173, 0) 45%),
      radial-gradient(ellipse at 60% 50%, var(--leaf-tone) 0%, rgba(67, 53, 42, 0.55) 45%, rgba(26, 22, 19, 0) 72%);
  }
  .brand {
    position: absolute;
    display: flex;
    align-items: center;
    gap: 12px;
    color: var(--gold);
    font-weight: 600;
    text-transform: uppercase;
  }
  .brand-dot {
    flex: none;
    border-radius: 50%;
    background: var(--gold);
  }
  .brand-name { line-height: 1.35; white-space: nowrap; }
  .card-front .brand {
    left: 60px;
    top: 118px;
    font-size: 19px;
    letter-spacing: 0.12em;
  }
  .card-front .brand-dot { width: 34px; height: 34px; }

  /* Back */
  .divider {
    position: absolute;
    inset: 0;
    width: 100%;
    height: 100%;
  }
  .gold-band {
    position: absolute;
    background: linear-gradient(100deg, var(--gold-deep), var(--gold-light) 45%, var(--gold) 70%, var(--gold-deep));
  }
  .gold-band--top {
    top: 0;
    right: 0;
    width: 150px;
    height: 12px;
    clip-path: polygon(12px 0, 100% 0, 100% 100%, 0 100%);
  }
  .gold-band--side {
    right: 0;
    bottom: 0;
    width: 12px;
    height: 150px;
  }
  .card-back .brand {
    left: 34px;
    top: 190px;
    font-size: 12px;
    letter-spacing: 0.1em;
  }
  .card-back .brand-dot { width: 22px; height: 22px; }
  .contact-block {
    position: absolute;
    left: 300px;
    top: 70px;
  }
  .company-name {
    color: var(--gold);
    font-size: 17px;
    font-weight: 500;
    white-space: nowrap;
  }
  .company-slogan {
    color: var(--blush);
    font-size: 11px;
    margin: 2px 0 10px;
  }
  .contact-list { list-style: none; }
  .contact-list li {
    display: flex;
    align-items: center;
    gap: 7px;
    color: var(--text-soft);
    font-size: 9px;
    line-height: 17px;
  }
  .contact-list svg { width: 10px; height: 10px; flex: none; }
</style>
</head>
<body>
<main class="sheet">

  <section class="card card-front" aria-label="Card front">
    <div class="leaf-decoration" role="img" aria-label="Faint tropical leaves in dark bronze with a blush pink glow"></div>
    <div class="brand">
      <span class="brand-dot"></span>
      <span class="brand-name">Meadow and Willow<br>Massage Studio</span>
    </div>
  </section>

  <section class="card card-back" aria-label="Card back">
    <svg class="divider" viewBox="0 0 525 300" aria-hidden="true">
      <defs>
        <linearGradient id="divider-gold" x1="0" y1="0" x2="1" y2="1">
          <stop offset="0" stop-color="#8a6420"/>
          <stop offset="0.5" stop-color="#f1d27a"/>
          <stop offset="1" stop-color="#8a6420"/>
        </linearGradient>
      </defs>
      <line x1="190" y1="40" x2="330" y2="270" stroke="url(#divider-gold)" stroke-width="1.6"/>
    </svg>
    <div class="gold-band gold-band--top"></div>
    <div class="gold-band gold-band--side"></div>

    <div class="brand">
      <span class="brand-dot"></span>
      <span class="brand-name">Meadow and Willow<br>Massage Studio</span>
    </div>

    <div class="contact-block">
      <p class="company-name">Meadow and Willow</p>
      <p class="company-slogan">Relax · Restore</p>
      <ul class="contact-list">
        <li>
          <svg viewBox="0 0 10 10" aria-hidden="true"><path d="M2 1 L4 1 L4.6 3 L3.5 3.8 Q4.5 5.6 6.2 6.5 L7 5.4 L9 6 L9 8 Q5 9 2.5 6.5 Q0.8 4.5 2 1 Z" fill="#d8d2c8"/></svg>
          000 000 0000
        </li>
        <li>
          <svg viewBox="0 0 10 10" aria-hidden="true"><circle cx="5" cy="5" r="4" fill="none" stroke="#d8d2c8"/><path d="M1 5 H9 M5 1 Q2.5 5 5 9 M5 1 Q7.5 5 5 9" fill="none" stroke="#d8d2c8" stroke-width="0.7"/></svg>
          meadowwillow.com
        </li>
        <li>
          <svg viewBox="0 0 10 10" aria-hidden="true"><rect x="0.5" y="2" width="9" height="6" fill="none" stroke="#d8d2c8"/><path d="M0.5 2 L5 5.5 L9.5 2" fill="none" stroke="#d8d2c8"/></svg>
          hello@meadowwillow.com
        </li>
      </ul>
    </div>
  </section>

</main>
</body>
</html>
```